Tralha Caixa Website

Tralha Caixa is a brazilian Self Storage in a Box where customers can store all the clutter that they have out of their houses. We deliver one or more boxes at their homes, they fill the boxes with their stuff and we store it for them.

"Tralha" means something like "mess" in portuguese. So the name would means something like "Junk Crate" or "Junk Crate".

How it works:
1) The customer asks for 1 or more boxes.
2) Tralha Caixa leaves the boxes at their houses
3) The clients fill the boxes with their stuff
4) Customers call Tralha Caixa for the pick up
5) We get the boxes and store them
6) When the customer wants the box back they can order it online or by phone and wait for the box delivery.
-

We have already produced a flyer to launch the service. You can see this flyer at "Project Files".

We want the website to have a startup "look and fell". Here are some websites of similar services that we like very much.
- www.stowquill.example
- www.pakvale.example

We are planning this launching website to have only 2 pages. The Landing Page and a FAQ page. We are producing an explainer video. The proposed designs must think about a special place to place the video.

We are still writing it´s content but you can use the flyer as a reference.

Thanks.
Updates

Reason: The project was refundable but as we have already received good design options, now we are turning it to Non Refundable and giving more time for new designers to send their proposals. Thanks.

Target Market(s)

Young couples having kids
Students
Families in need of more space at home

Industry/Entity Type

Store

Requirements
Must have
• Special place to place the explainer video (still being produced).

How it works drawing. You can use the one on the flyer or draw a new one (recomended).

Transparent box drawings (showing it´s content). I will serve to show the clients what they can store with the service.

Clutter Room Before/After Pic/drawings (showing how the service can benefit the client).

```html
<!DOCTYPE html>
<html lang="en">
<head>
<meta charset="utf-8">
<title>Tralha Caixa — How We Work</title>
<link href="https://fonts.googleapis.com/css2?family=Pathway+Gothic+One&family=Arimo:wght@400;700&family=Open+Sans:wght@400;700&display=swap" rel="stylesheet">
<style>
  :root {
    --page-bg: #e6eaec;
    --card-bg: #ffffff;
    --card-fold: #dfe3e6;
    --heading-blue: #3f7fa8;
    --rule: #c9cfd3;
    --muted: #9aa1a6;
    --body-text: #4a4a4a;
    --slate: #4d5d6e;
    --coral: #d9553f;
    --icon-black: #111111;
    --cal-red: #e0573d;
    --cal-blue: #4e8fcf;
    --dot-red: #e2504a;
    --dot-yellow: #f2c230;
    --dot-teal: #3bb3b0;
    --player-bar: #1e1e1e;
    --player-text: #d8d8d8;
  }
  * { box-sizing: border-box; margin: 0; padding: 0; }
  html, body { width: 1200px; height: 547px; overflow: hidden; }
  body { background: var(--page-bg); position: relative; font-family: "Arimo", Arial, sans-serif; }

  .section-title {
    position: absolute; left: 358px; top: 4px; width: 476px;
    display: flex; align-items: center; gap: 8px;
    font-family: "Pathway Gothic One", "Arial Narrow", sans-serif;
    font-size: 11px; letter-spacing: .5px; color: var(--muted);
  }
  .section-title::before, .section-title::after { content: ""; flex: 1; height: 1px; background: var(--rule); }

  .step-card {
    position: absolute; top: 36px; width: 108px;
    background: var(--card-bg); text-align: center;
    padding: 0 8px;
    clip-path: polygon(0 0, calc(100% - 10px) 0, 100% 10px, 100% 100%, 0 100%);
  }
  .step-card::after {
    content: ""; position: absolute; right: 0; top: 0; width: 10px; height: 10px;
    background: linear-gradient(45deg, var(--card-fold) 50%, transparent 50%);
  }
  .step-card .icon { display: block; margin: 0 auto; }
  .step-title {
    font-family: "Pathway Gothic One", "Arial Narrow", sans-serif;
    font-weight: 400; font-size: 11.5px; line-height: 10px;
    color: var(--heading-blue); text-transform: uppercase;
  }
  .step-text { font-size: 8px; line-height: 10.5px; color: var(--body-text); margin-top: 5px; }

  .card-store { left: 358px; height: 165px; }
  .card-choose { left: 481px; height: 146px; }
  .card-time { left: 604px; height: 146px; }
  .card-return { left: 727px; height: 155px; }

  .people-illustration {
    width: 48px; height: 56px; margin: 6px auto 10px;
    background: linear-gradient(135deg, #c9553a, #6c5a8a 55%, #e0a33c);
    border-radius: 4px;
  }

  .video-section {
    position: absolute; left: 358px; top: 216px; width: 476px; height: 331px;
    background: radial-gradient(ellipse at 50% 35%, #e6e6e6 0%, #d2d2d2 55%, #c4c4c4 100%);
    overflow: hidden;
  }
  .skyline {
    position: absolute; left: 150px; bottom: 0; width: 60px; height: 70px;
    background: linear-gradient(to top, #bdbdbd, rgba(200,200,200,0));
  }
  .tagline { position: absolute; left: 25px; top: 170px; font-family: "Open Sans", Arial, sans-serif; }
  .tagline span { display: table; color: #fff; font-size: 12px; line-height: 15px; padding: 0 3px; margin-bottom: 1px; }
  .tagline .lead { background: var(--slate); font-weight: 700; font-size: 13px; }
  .tagline .line { background: var(--coral); }

  .video-player {
    position: absolute; left: 191px; top: 169px; width: 261px; height: 146px;
    background: #f4f4f4; box-shadow: 0 14px 12px -8px rgba(0,0,0,.45);
  }
  .player-chrome { height: 20px; background: linear-gradient(#e8e8e8, #cfcfcf); border-bottom: 1px solid #b5b5b5; }
  .player-screen {
    position: absolute; left: 12px; top: 30px; width: 237px; height: 88px;
    display: flex; gap: 6px;
  }
  .player-screen .poster { flex: 1; }
  .poster-a { background: linear-gradient(#bcd3e6, #6b7d8a 70%, #2b2b2b); }
  .poster-b { background: linear-gradient(#3a3a3a, #111); }
  .poster-c { background: linear-gradient(#6a5a3e, #1a1a1a); }
  .poster-d { background: linear-gradient(#c9bb97, #5a4a35); }
  .play-badge { position: absolute; left: 113px; top: 62px; }
  .control-bar {
    position: absolute; left: 0; bottom: 0; width: 100%; height: 25px;
    background: var(--player-bar); display: flex; align-items: center; gap: 10px; padding: 0 8px;
    font-size: 8px; color: var(--player-text); font-weight: 700;
  }
  .control-bar .spacer { flex: 1; }
  .brand-name { font-size: 8px; font-weight: 700; color: #8a8a8a; }
</style>
</head>
<body>
  <h2 class="section-title">HOW WE WORK ?</h2>

  <article class="step-card card-store">
    <div class="people-illustration" role="img" aria-label="Illustration of a family carrying belongings to a storage box"></div>
    <h3 class="step-title">Know for yourself what you want to store ?</h3>
    <p class="step-text">Maintain your own record about all the items by taking a snap and storing that image online.</p>
  </article>

  <article class="step-card card-choose">
    <svg class="icon" width="36" height="36" viewBox="0 0 36 36" style="margin:15px auto 10px">
      <rect width="36" height="36" rx="7" fill="var(--icon-black)"/>
      <rect x="7" y="11" width="14" height="11" fill="#fff"/>
      <path d="M22 14h5l3 4v4h-8z" fill="#fff"/>
      <circle cx="11" cy="24" r="2.3" fill="#fff"/><circle cx="25" cy="24" r="2.3" fill="#fff"/>
    </svg>
    <h3 class="step-title">You just choose and fill the items,we will pick them up.</h3>
    <p class="step-text">Decide on your own about the storage plan you are going to go for.</p>
  </article>

  <article class="step-card card-time">
    <svg class="icon" width="32" height="30" viewBox="0 0 32 30" style="margin:11px auto 4px">
      <rect x="1" y="3" width="30" height="26" rx="3" fill="#fff" stroke="#bbb"/>
      <rect x="1" y="3" width="30" height="8" rx="3" fill="var(--cal-red)"/>
      <rect x="8" y="0" width="3" height="6" rx="1" fill="#666"/><rect x="21" y="0" width="3" height="6" rx="1" fill="#666"/>
      <g fill="var(--cal-blue)">
        <rect x="5" y="14" width="4" height="3"/><rect x="11" y="14" width="4" height="3"/><rect x="17" y="14" width="4" height="3"/><rect x="23" y="14" width="4" height="3"/>
        <rect x="5" y="19" width="4" height="3"/><rect x="11" y="19" width="4" height="3"/><rect x="17" y="19" width="4" height="3"/><rect x="23" y="19" width="4" height="3"/>
        <rect x="5" y="24" width="4" height="3"/><rect x="11" y="24" width="4" height="3"/>
      </g>
    </svg>
    <h3 class="step-title">You decide the time when your items will be picked up ?</h3>
    <p class="step-text">Just schedule the pickup of items and relax .Your items are at safe hands.</p>
  </article>

  <article class="step-card card-return">
    <svg class="icon" width="50" height="56" viewBox="0 0 50 56" style="margin:12px auto 6px">
      <rect x="8" y="1" width="34" height="34" rx="7" fill="#fff" stroke="#cfcfcf"/>
      <rect x="14" y="12" width="13" height="10" fill="var(--icon-black)"/>
      <path d="M28 15h5l3 4v3h-8z" fill="var(--icon-black)"/>
      <circle cx="18" cy="24" r="2.2" fill="var(--icon-black)"/><circle cx="31" cy="24" r="2.2" fill="var(--icon-black)"/>
      <rect x="1" y="42" width="12" height="12" rx="2" fill="var(--dot-red)"/>
      <rect x="19" y="42" width="12" height="12" rx="2" fill="var(--dot-yellow)"/>
      <rect x="37" y="42" width="12" height="12" rx="2" fill="var(--dot-teal)"/>
      <g fill="#222"><rect x="4" y="46" width="5" height="4"/><rect x="22" y="46" width="5" height="4"/><rect x="40" y="46" width="5" height="4"/></g>
    </svg>
    <h3 class="step-title">Demand the return whenever you want it.</h3>
    <p class="step-text">On demand return of your prized possessions.</p>
  </article>

  <section class="video-section">
    <div class="skyline" role="img" aria-label="Faint city skyline backdrop"></div>
    <div class="tagline">
      <span class="lead">Visualize</span>
      <span class="line">Our way of doing things</span>
      <span class="line">to ensure</span>
      <span class="line">Customer convenience.</span>
    </div>

    <div class="video-player">
      <div class="player-chrome"></div>
      <div class="player-screen" role="img" aria-label="Explainer video frame showing a screen recording of the storage catalogue">
        <div class="poster poster-a"></div>
        <div class="poster poster-b"></div>
        <div class="poster poster-c"></div>
        <div class="poster poster-d"></div>
      </div>
      <svg class="play-badge" width="34" height="26" viewBox="0 0 34 26">
        <rect width="34" height="26" rx="4" fill="rgba(0,0,0,.75)"/>
        <path d="M13 7l10 6-10 6z" fill="#fff"/>
      </svg>
      <div class="control-bar">
        <svg width="12" height="12" viewBox="0 0 12 12"><path d="M2 1l9 5-9 5z" fill="#9a9a9a"/></svg>
        <svg width="14" height="12" viewBox="0 0 14 12"><path d="M1 4h3l4-3v10l-4-3H1z" fill="#9a9a9a"/><path d="M10 3q2 3 0 6" stroke="#9a9a9a" fill="none"/></svg>
        <span>00:00 / 52:32</span>
        <span class="spacer"></span>
        <svg width="10" height="10" viewBox="0 0 10 10"><circle cx="5" cy="5" r="4.5" fill="#8a8a8a"/></svg>
        <span class="brand-name">ReelPort</span>
        <svg width="12" height="12" viewBox="0 0 12 12" fill="none" stroke="#9a9a9a" stroke-width="1.5"><path d="M1 4V1h3M8 1h3v3M11 8v3H8M4 11H1V8"/></svg>
      </div>
    </div>
  </section>
</body>
</html>
```